Graphic Banner Design - 2.5' x 6' - High Tech Company

We are in need of a banner design for an outdoor sign that will be used at sponsorship events.

Size
2.5' x 6'

The company is a high tech company, and the design will be used for action sports events. So lining up to that would be good.

Tag line to be incorporated...
"Extreme IT Services for Extreme Needs."

Target Market(s)

Business Owners, Entrepreneurs, IT Professionals.

Industry/Entity Type

Information Technology

Logo Text

Brindlex

Colors

Designer to choose colors to be used in the design.

Requirements
Must have
• Must feel young and vibrant, fit in to an action sports event and just be out of this world awesome.
• In the world of the IT, we are the Castavelli. Fast, Awesome, not necessarily cheap, but you know it will do what you want extremely well. Not for everyone, but always desired.

```html
<!DOCTYPE html>
<html lang="en">
<head>
<meta charset="UTF-8">
<title>Brindlex – Extreme IT Services Banner</title>
<link rel="stylesheet" href="https://fonts.googleapis.com/css2?family=Cinzel:wght@900&family=Montserrat:wght@400&display=swap">
<style>
  :root {
    --sky-deep: #2f7fd0;
    --sky-mid: #3aa6e6;
    --sky-bright: #33c3f2;
    --wave-light: rgba(120, 215, 250, 0.35);
    --wave-soft: rgba(255, 255, 255, 0.12);
    --headline-ink: #2b1f6a;
    --brand-ink: #121212;
    --illustration-desk: #c9d7e6;
    --illustration-hands: #f2c48c;
    --illustration-sleeve: #f5b731;
  }
  html, body {
    margin: 0;
    padding: 0;
    overflow: hidden;
  }
  .banner {
    position: relative;
    width: 1200px;
    height: 500px;
    overflow: hidden;
    background: linear-gradient(160deg, var(--sky-deep) 0%, var(--sky-mid) 45%, var(--sky-bright) 80%, var(--sky-mid) 100%);
  }
  .banner__waves {
    position: absolute;
    inset: 0;
    width: 100%;
    height: 100%;
  }
  .illustration {
    position: absolute;
    opacity: 0.85;
  }
  .illustration--laptop {
    left: 0;
    top: 112px;
    width: 230px;
    height: 290px;
    background: linear-gradient(135deg, var(--illustration-desk) 0%, #e8eef5 60%, var(--illustration-hands) 100%);
    border-radius: 0 8px 8px 0;
  }
  .illustration--tablet {
    right: 0;
    top: 80px;
    width: 160px;
    height: 266px;
    background: linear-gradient(200deg, var(--illustration-sleeve) 0%, var(--illustration-hands) 45%, #e9eef4 100%);
    border-radius: 8px 0 0 8px;
  }
  .headline {
    position: absolute;
    left: 240px;
    top: 98px;
    width: 800px;
    margin: 0;
    font-family: "Cinzel", serif;
    font-weight: 900;
    font-size: 60px;
    line-height: 96px;
    letter-spacing: 1px;
    text-transform: uppercase;
    text-align: center;
    white-space: nowrap;
    color: var(--headline-ink);
  }
  .brand {
    position: absolute;
    left: 0;
    width: 1196px;
    top: 400px;
    margin: 0;
    text-align: center;
    font-family: "Montserrat", sans-serif;
    font-weight: 400;
    font-size: 44px;
    line-height: 52px;
    color: var(--brand-ink);
  }
</style>
</head>
<body>
  <main class="banner">
    <svg class="banner__waves" viewBox="0 0 1200 500" preserveAspectRatio="none" aria-hidden="true">
      <path d="M0 60 C 250 20, 420 120, 640 70 S 1000 10, 1200 60 L 1200 0 L 0 0 Z" fill="var(--wave-soft)"/>
      <path d="M300 0 C 420 160, 560 260, 700 330 S 900 460, 980 500 L 1200 500 L 1200 380 C 1040 340, 880 220, 760 120 S 560 10, 520 0 Z" fill="var(--wave-light)"/>
      <path d="M0 420 C 200 380, 420 470, 640 430 S 1000 360, 1200 420 L 1200 500 L 0 500 Z" fill="var(--wave-soft)"/>
    </svg>

    <div class="illustration illustration--laptop" role="img" aria-label="Illustration of hands typing on a laptop and using a mouse"></div>
    <div class="illustration illustration--tablet" role="img" aria-label="Illustration of hands holding and tapping a tablet"></div>

    <h1 class="headline">Extreme IT Services<br>for Extreme Needs.</h1>

    <p class="brand">Brindlex</p>
  </main>
</body>
</html>
```